Psychology practice - information brochure/flyer - half A4 page folded (4 sides)

We need a brochure/flyer to market our psychology service to GPs (Doctors). We need to demonstrate to the doctors that we are the right choice for their patients, and that we cover a large range of services so all of their patients needs are met. We will demonstrate this by listing our range of services and our team of psychologists. We have two locations in Sydney and offer high end services. I've attached our company logo but we remain flexible regarding the style of the brochures. I will provide more details (services, locations & psychologist credentials) once our preferred brochure design has been selected.

```html
<!DOCTYPE html>
<html lang="en">
<head>
<meta charset="utf-8">
<title>Clear Harbour Clinical Psychology – GP Referral Flyer</title>
<link href="https://fonts.googleapis.com/css2?family=Questrial&family=Montserrat:wght@700&display=swap" rel="stylesheet">
<style>
  :root {
    --page-bg: #d6d6d6;
    --brand-blue: #2a66a8;
    --brand-blue-deep: #225a97;
    --brand-yellow: #f7c21b;
    --band-orange: #ec9a2c;
    --sun-cream: #fbecc8;
    --sun-gold: #efb45a;
    --sand-amber: #e49a3e;
    --sea-haze: #c98a47;
    --white: #ffffff;
    --logo-grey: #4a4a4a;
  }
  * { box-sizing: border-box; margin: 0; padding: 0; }
  html, body {
    width: 1200px; height: 1200px; overflow: hidden;
    background: var(--page-bg);
    font-family: "Questrial", "Century Gothic", sans-serif;
  }
  .flyer {
    position: absolute; left: 60px; top: 218px;
    width: 1080px; height: 764px;
    display: flex;
    box-shadow: 0 6px 18px rgba(0,0,0,0.18);
  }
  .info-panel {
    position: relative; width: 540px; height: 100%;
    background: linear-gradient(180deg, var(--brand-blue) 0%, var(--brand-blue-deep) 100%);
    color: var(--white); text-align: center;
  }
  .info-panel .line { position: absolute; left: 0; width: 100%; }
  .eyebrow { top: 94px; font-size: 31px; letter-spacing: 0.5px; }
  .headline {
    top: 134px; font-family: "Montserrat", sans-serif; font-weight: 700;
    font-size: 51px; color: var(--brand-yellow); letter-spacing: 1px;
  }
  .location { top: 198px; font-size: 30px; }
  .divider {
    position: absolute; left: 66px; width: 420px;
    border-top: 2px dashed rgba(255,255,255,0.75);
  }
  .divider--top { top: 282px; }
  .divider--bottom { top: 451px; }
  .services { top: 327px; font-size: 29px; line-height: 34px; }
  .company { top: 516px; font-size: 19px; letter-spacing: 0.3px; }
  .contact-list {
    position: absolute; left: 100px; top: 548px; list-style: none; text-align: left;
  }
  .contact-list li { display: flex; align-items: flex-start; gap: 14px; font-size: 18px; line-height: 22px; margin-bottom: 7px; }
  .contact-list .icon { width: 22px; flex: none; display: flex; justify-content: center; padding-top: 1px; }
  .contact-list .phone {
    font-family: "Montserrat", sans-serif; font-weight: 700; font-size: 38px;
    line-height: 44px; color: var(--brand-yellow); margin-bottom: 10px; align-items: center;
    margin-left: 6px;
  }
  .contact-list .phone .icon { width: 30px; }
  .visual-panel { position: relative; width: 540px; height: 100%; }
  .photo-area {
    position: absolute; inset: 0;
    background:
      linear-gradient(180deg, rgba(0,0,0,0) 45%, rgba(120,70,30,0.18) 50%, rgba(0,0,0,0) 58%),
      radial-gradient(ellipse at 55% 12%, var(--sun-cream) 0%, var(--sun-gold) 45%, var(--sand-amber) 100%);
  }
  .brand-name {
    position: absolute; right: 36px; top: 70px;
    display: flex; align-items: center; gap: 10px;
    font-size: 33px; line-height: 34px; color: var(--logo-grey);
  }
  .brand-name .mark { width: 14px; height: 14px; background: var(--brand-yellow); flex: none; }
  .tagline-band {
    position: absolute; left: 0; top: 570px; width: 100%; height: 135px;
    background: var(--band-orange); color: var(--white);
    display: flex; flex-direction: column; justify-content: center; align-items: center;
    font-size: 28px; line-height: 34px; text-align: center;
  }
</style>
</head>
<body>
  <main class="flyer">
    <section class="info-panel">
      <p class="line eyebrow">FOR GPs &amp; THEIR PATIENTS</p>
      <h1 class="line headline">EXPERT CARE</h1>
      <p class="line location">AT TWO SYDNEY LOCATIONS</p>
      <div class="divider divider--top"></div>
      <p class="line services">ADULT, CHILD &amp; FAMILY THERAPY<br>FROM OUR TEAM OF<br>REGISTERED PSYCHOLOGISTS</p>
      <div class="divider divider--bottom"></div>
      <p class="line company">CLEAR HARBOUR CLINICAL PSYCHOLOGY</p>
      <ul class="contact-list">
        <li class="phone">
          <span class="icon"><svg width="28" height="30" viewBox="0 0 28 30"><rect x="1" y="1" width="26" height="28" rx="5" fill="#f7c21b"/><path d="M9 7c-2 1-2 4 0 8s5 7 8 8c2 1 4 0 4-2l-3-3-2 1c-2-1-4-3-5-5l1-2-3-3z" fill="#2a66a8"/></svg></span>
          (02) 5550 1472
        </li>
        <li>
          <span class="icon"><svg width="16" height="22" viewBox="0 0 16 22"><path d="M8 1a7 7 0 0 0-7 7c0 5 7 13 7 13s7-8 7-13a7 7 0 0 0-7-7z" fill="#f7c21b"/><circle cx="8" cy="8" r="2.6" fill="#2a66a8"/></svg></span>
          <span>Suite 1, Level 1, 14 Parkview Lane<br>Westmere NSW 2299</span>
        </li>
        <li>
          <span class="icon"><svg width="22" height="16" viewBox="0 0 22 16"><rect x="1" y="1" width="20" height="14" fill="#f7c21b"/><path d="M1 1l10 8 10-8" fill="none" stroke="#2a66a8" stroke-width="1.6"/></svg></span>
          <span>hello@clearharbourpsych.example</span>
        </li>
        <li>
          <span class="icon"><svg width="20" height="20" viewBox="0 0 20 20" fill="none" stroke="#f7c21b" stroke-width="1.5"><circle cx="10" cy="10" r="8.5"/><ellipse cx="10" cy="10" rx="3.8" ry="8.5"/><path d="M1.5 10h17M3 5.5h14M3 14.5h14"/></svg></span>
          <span>www.clearharbourpsych.example</span>
        </li>
      </ul>
    </section>
    <section class="visual-panel">
      <div class="photo-area" role="img" aria-label="Photo of a family running hand in hand along the beach at sunset"></div>
      <div class="brand-name"><span class="mark"></span><span>Clear Harbour<br>Clinical Psychology</span></div>
      <p class="tagline-band">WORKING TOGETHER TO<br>ACHIEVE A BETTER QUALITY OF LIFE</p>
    </section>
  </main>
</body>
</html>
```